New Plumbing Company

We are looking for a smart and creative business card design for our new plumbing company. We are looking for creativity and originality in our business cards.

Industry/Entity Type

Plumbing

Contact Information for Business Card

Crestline Plumbing
Peter Halvane
Managing Director
Telephone Number : 0481529604
Email : service@crestlineplumbing.com.au
Website : www.crestlineplumbing.com.au
Lic. 508264K

Colors
0692cd
33a6d7
000000

Requirements
Must have
• I want the business card to be designed on a black background using the blue tones i have selected as seen in the company logo.

```html
<!DOCTYPE html>
<html lang="en">
<head>
<meta charset="utf-8">
<title>Crestline Plumbing – Business Card</title>
<link href="https://fonts.googleapis.com/css2?family=Arimo:wght@400;700&display=swap" rel="stylesheet">
<style>
  :root {
    --page-bg: #e4e4e4;
    --card-black: #000000;
    --brand-blue: #0692cd;
    --brand-light: #33a6d7;
    --deep-teal: #003047;
    --glow-blue: #004d72;
    --text-white: #ffffff;
  }
  * { margin: 0; padding: 0; box-sizing: border-box; }
  html, body {
    width: 1200px;
    height: 1199px;
    overflow: hidden;
    background: var(--page-bg);
    font-family: "Arimo", Arial, sans-serif;
  }
  .business-card {
    position: absolute;
    left: 183px;
    top: 305px;
    width: 843px;
    height: 481px;
    border-radius: 22px;
    overflow: hidden;
    background: var(--card-black);
    color: var(--text-white);
  }
  .card-backdrop {
    position: absolute;
    inset: 0;
    background: linear-gradient(90deg,
      var(--card-black) 0%,
      #000a0f 30%,
      #001c29 50%,
      var(--deep-teal) 65%,
      var(--glow-blue) 78%,
      #00263a 90%,
      var(--card-black) 100%);
  }
  .holder-name {
    position: absolute;
    left: 62px;
    top: 58px;
    font-size: 31px;
    font-weight: 700;
  }
  .holder-title {
    position: absolute;
    left: 60px;
    top: 103px;
    font-size: 24px;
    font-weight: 400;
  }
  .brand {
    position: absolute;
    left: 56px;
    top: 213px;
    display: flex;
    align-items: center;
    gap: 16px;
  }
  .brand-mark {
    width: 70px;
    height: 70px;
    border: 4px solid var(--brand-blue);
    border-radius: 50%;
  }
  .brand-name {
    font-size: 30px;
    font-weight: 400;
  }
  .contact-line {
    position: absolute;
    display: flex;
    align-items: center;
    font-size: 25px;
    font-weight: 400;
  }
  .contact-phone { left: 59px; top: 383px; }
  .contact-email { left: 47px; top: 421px; font-size: 26px; }
  .contact-icon { flex: none; }
  .contact-phone .contact-icon { margin-right: 16px; }
  .contact-email .contact-icon { margin-right: 15px; }
  .licence {
    position: absolute;
    right: 44px;
    top: 419px;
    font-size: 25px;
    font-weight: 400;
  }
</style>
</head>
<body>
  <section class="business-card">
    <div class="card-backdrop" role="img" aria-label="Decorative blue wave sweeping across the black card"></div>

    <h1 class="holder-name">Peter Halvane</h1>
    <p class="holder-title">Managing Director</p>

    <div class="brand">
      <span class="brand-mark"></span>
      <span class="brand-name">Crestline Plumbing</span>
    </div>

    <p class="contact-line contact-phone">
      <svg class="contact-icon" width="18" height="25" viewBox="0 0 18 25" aria-hidden="true">
        <rect x="1" y="1" width="16" height="23" rx="1.5" fill="none" stroke="#fff" stroke-width="2"/>
        <rect x="4" y="4" width="10" height="6" fill="none" stroke="#fff" stroke-width="1.5"/>
        <path d="M4 13h10M4 16h10M4 19h10M7.5 12v9M10.5 12v9" stroke="#fff" stroke-width="1.2"/>
      </svg>
      0481529604
    </p>
    <p class="contact-line contact-email">
      <svg class="contact-icon" width="29" height="19" viewBox="0 0 29 19" aria-hidden="true">
        <rect width="29" height="19" fill="#fff"/>
        <path d="M0 0 L14.5 11 L29 0" fill="none" stroke="#000" stroke-width="2.2"/>
      </svg>
      service@crestlineplumbing.com.au
    </p>

    <p class="licence">Lic. 508264K</p>
  </section>
</body>
</html>
```